Quillfield Gallery Ridge Campus

Design cover and inside pages. - will fill in the rest later. I just have some ideas here. This is a marketing brochure for a new building - raising money. Should look professional - but this is an art gallery, so can have color. I wouldn't also mind seeing some chrome effects. I put some samples of fun ideas, but I am open. This is to get people exciting to give to the campaign to raise money for the new building
Target Market(s)
People who would like to donate to a new art gallery - the local community
Requirements
Must have
- The end product, after it is cut down from full bleed, should be 8.25 X 8.25.
Nice to have
- Should be modern and and exciting. The one thing is to show the problem and how we are going to solve it.. Something like "challenge" and resolution"..
- Would like it to go along with this idea of evolve - something new and improved and exciting.. with a very modern look. YOu will see that the logo is three different gradients of orange.. these can change to another color - it doesn't have to be orange.. I would like to see less orange used. The font on the old building is art deco.. so I see that the font for this should be non-serif
Should not have
- I have had designers use the logo as an overlay over pictures - I would like to get away from that.

```html
<!DOCTYPE html>
<html lang="en">
<head>
<meta charset="utf-8">
<title>Quillfield Gallery Ridge Campus — Brochure Spreads</title>
<link href="https://fonts.googleapis.com/css2?family=EB+Garamond:wght@500;600&family=PT+Sans:wght@400;700&display=swap" rel="stylesheet">
<style>
  :root {
    --stage: #3a3637;
    --paper: #ffffff;
    --orange: #e8712a;
    --orange-deep: #e3631f;
    --gold: #e3ad2f;
    --pink: #e8479a;
    --magenta: #e13f8e;
    --ink: #1c1c1c;
    --ink-soft: #333333;
    --grey-page: #d3d3d3;
    --black-band: #0d0d0d;
  }
  * { box-sizing: border-box; margin: 0; padding: 0; }
  html, body { width: 1200px; height: 1200px; overflow: hidden; }
  body { background: var(--stage); position: relative; font-family: "PT Sans", sans-serif; }

  .spread { position: absolute; left: 35px; width: 1127px; height: 435px; background: var(--paper); overflow: hidden; }
  .spread--cover { top: 118px; }
  .spread--inside { top: 600px; }
  .abs { position: absolute; }

  /* cover */
  .cover-wash {
    left: 0; top: 0; width: 690px; height: 435px;
    background:
      radial-gradient(ellipse 320px 200px at 260px 60px, #f6b043 0%, rgba(246,176,67,0) 70%),
      radial-gradient(ellipse 260px 180px at 520px 150px, #f39a4a 0%, rgba(243,154,74,0) 70%),
      radial-gradient(ellipse 380px 260px at 180px 360px, #ea4fa0 0%, rgba(234,79,160,0) 75%),
      linear-gradient(160deg, #f5a83a 0%, #f28c55 35%, #e960a0 62%, #e448a0 100%);
  }
  .guild-mark { display: flex; align-items: center; gap: 8px; color: #ffffff; font-family: "PT Sans", sans-serif; font-weight: 700; letter-spacing: 3px; text-transform: uppercase; }
  .guild-mark__dot { width: 48px; height: 48px; border-radius: 50%; background: var(--orange); flex: none; }
  .guild-mark__name { line-height: 1; white-space: nowrap; }
  .guild-mark__name span { display: block; }
  .guild-mark__name .big { font-size: 30px; }
  .guild-mark__name .small { font-size: 13px; margin-top: 4px; letter-spacing: 3.5px; }
  .cover-mark { left: 177px; top: 322px; }

  .black-band { left: 563px; top: 288px; width: 264px; height: 83px; background: var(--black-band); display: flex; align-items: center; padding-left: 34px; }
  .black-band .guild-mark__dot { width: 44px; height: 44px; }
  .black-band .big { font-size: 27px; }
  .black-band .small { font-size: 12px; }

  .front-page { left: 689px; top: 0; width: 438px; height: 435px; background: var(--paper); }
  .building-art { left: 0; top: 70px; width: 438px; height: 365px;
    background: linear-gradient(180deg, #cfdcdf 0%, #d8dcd9 30%, #a1806a 55%, #9a9c9f 78%, #c9cbcd 100%); }
  .campus-tag { right: 47px; top: 30px; font-family: "EB Garamond", serif; font-weight: 500; font-size: 16px; color: var(--orange); letter-spacing: 0.5px; text-transform: uppercase; }
  .gallery-title { left: 24px; top: 47px; font-family: "EB Garamond", serif; font-weight: 600; font-size: 34px; color: var(--orange-deep); letter-spacing: 1px; text-transform: uppercase; line-height: 1; white-space: nowrap; }
  .gallery-sub { left: 24px; top: 85px; font-size: 13.5px; color: var(--ink); text-transform: uppercase; line-height: 18px; letter-spacing: 0.2px; }

  /* inside */
  .garden-art { left: 45px; top: 24px; width: 480px; height: 264px;
    background: linear-gradient(180deg, #9b928a 0%, #8a7358 40%, #7c6a55 60%, #6c6c6c 80%, #d0d0d0 100%); }
  .inspiration-board { left: 25px; top: 312px; width: 166px; height: 108px; border-bottom: 1px solid #999;
    background: repeating-linear-gradient(90deg, #f2f2f2 0 36px, #ffffff 36px 42px); }
  .inspiration-board .label { position: absolute; left: 0; top: -9px; font-size: 5px; color: #444; text-transform: uppercase; }
  .inspiration-board .views { position: absolute; right: 0; bottom: -8px; font-size: 5px; color: #444; text-transform: uppercase; }
  .section-title { left: 203px; top: 304px; font-family: "EB Garamond", serif; font-weight: 600; font-size: 26px; color: var(--orange-deep); text-transform: uppercase; letter-spacing: 0.5px; line-height: 1; }
  .body-copy { font-size: 7.4px; line-height: 10.1px; color: var(--ink-soft); text-align: justify; }
  .garden-copy { left: 203px; top: 336px; width: 338px; }

  .right-page { left: 563px; top: 0; width: 564px; height: 424px;
    background: linear-gradient(90deg, var(--grey-page) 0%, #ededed 40%, #ffffff 75%); }
  .inside-mark { left: 34px; top: 72px; gap: 10px; z-index: 2; }
  .inside-mark .guild-mark__dot { width: 38px; height: 38px; }
  .inside-mark .guild-mark__name { color: var(--ink); }
  .inside-mark .big { font-size: 17px; letter-spacing: 1.5px; }
  .inside-mark .small { font-size: 8.5px; letter-spacing: 2px; margin-top: 3px; }
  .reception-photo { left: 249px; top: 24px; width: 326px; height: 244px;
    background: linear-gradient(160deg, #e4e7ea 0%, #bfc1c3 35%, #6a6a6c 55%, #d8d3c8 80%, #cfc8b8 100%); }
  .reception-frame { left: 23px; top: 166px; width: 243px; height: 87px; border: 1.5px solid var(--gold); }
  .reception-label { left: 34px; top: 176px; width: 222px; height: 68px; background: var(--gold);
    display: flex; align-items: center; justify-content: center;
    font-family: "EB Garamond", serif; font-weight: 600; font-size: 36px; color: #fbf3dc; }
  .col-head { font-weight: 700; font-size: 11.5px; color: var(--orange-deep); line-height: 1; }
  .challenge { left: 23px; top: 292px; width: 237px; }
  .resolution { left: 283px; top: 292px; width: 259px; }
  .challenge .body-copy, .resolution .body-copy { margin-top: 3px; }

  .color-strip { left: 0; top: 424px; width: 1127px; height: 11px;
    background: linear-gradient(90deg, #f0a14a 0%, #ee7a3a 20%, #f2a04a 35%, #e66a3c 50%, #f3b352 62%, #ec6e8d 78%, #e8a04c 90%, #f09048 100%); }
</style>
</head>
<body>

<section class="spread spread--cover">
  <div class="abs cover-wash" role="img" aria-label="Flowing orange and pink watercolour ink wash"></div>

  <div class="abs guild-mark cover-mark">
    <div class="guild-mark__dot"></div>
    <div class="guild-mark__name"><span class="big">Quillfield</span><span class="small">Gallery Guild</span></div>
  </div>

  <div class="abs front-page">
    <div class="abs building-art" role="img" aria-label="Sketch rendering of the new brick and glass gallery building with parking lot and cars"></div>
    <div class="abs campus-tag">Ridge Campus</div>
    <h1 class="abs gallery-title">Quillfield Gallery</h1>
    <p class="abs gallery-sub">An evolutionary new space to experience<br>the visual arts</p>
  </div>

  <div class="abs black-band">
    <div class="guild-mark">
      <div class="guild-mark__dot"></div>
      <div class="guild-mark__name"><span class="big">Quillfield</span><span class="small">Gallery Guild</span></div>
    </div>
  </div>
</section>

<section class="spread spread--inside">
  <div class="abs garden-art" role="img" aria-label="Sketch rendering of the sculpture garden courtyard with pergola, tables, trees and iron gate"></div>
  <div class="abs inspiration-board" role="img" aria-label="Design inspiration sketches and 3D views">
    <span class="label">Design inspiration</span>
    <span class="views">3D views</span>
  </div>
  <h2 class="abs section-title">Sculpture Garden</h2>
  <p class="abs body-copy garden-copy">Lorem ipsum dolor sit amet, consectetur adipiscing elit. Ut nibh leo, cursus et laoreet ac, lobortis vulputate orci. Nunc ultricies massa egestas malesuada pretium. Morbi congue sem ultricies dui lobortis dictum. Ut convallis quam diam, vel interdum dolor semper et. Morbi tincidunt fermentum sem sit amet iaculis. Sed ullamcorper egestas metus, quis luctus magna venenatis id. Aenean ultricies enim eget magna convallis, aliquet venenatis nisi varius. Sed varius eu lectus nec ullamcorper. Praesent ullamcorper, nulla sed lobortis ultrices, urna mi tincidunt turpis, non maximus eros ex ut eros. Aliquam tincidunt ut odio sed mollis. In et ante in nibh iaculis gravida. In arcu augue, hendrerit eget urna sit amet, mattis efficitur magna.</p>

  <div class="abs right-page">
    <div class="abs reception-photo" role="img" aria-label="Photo of the current reception desk with glass display cases and brochure rack"></div>
    <div class="abs guild-mark inside-mark">
      <div class="guild-mark__dot"></div>
      <div class="guild-mark__name"><span class="big">Quillfield</span><span class="small">Gallery Guild</span></div>
    </div>
    <div class="abs reception-frame"></div>
    <div class="abs reception-label">Reception</div>

    <div class="abs challenge">
      <h3 class="col-head">Challenge:</h3>
      <p class="body-copy">Lorem ipsum dolor sit amet, consectetur adipiscing elit. Ut nibh leo, cursus et laoreet ac, lobortis vulputate orci. Nunc ultricies massa egestas malesuada pretium. Morbi congue sem ultricies dui lobortis dictum. Ut convallis quam diam, vel interdum dolor semper et. Morbi tincidunt fermentum sem sit amet iaculis. Sed ullamcorper egestas metus, quis luctus magna venenatis id. Aenean ultricies enim eget magna convallis, aliquet venenatis nisi varius. Sed varius eu lectus nec ullamcorper. Praesent ullamcorper, nulla sed lobortis ultrices, urna mi tincidunt turpis, non maximus eros ex ut eros. Aliquam tincidunt ut odio sed mollis. In et ante in nibh iaculis gravida. In arcu augue, hendrerit eget urna sit amet, mattis efficitur magna.</p>
    </div>
    <div class="abs resolution">
      <h3 class="col-head">Resolution</h3>
      <p class="body-copy">Lorem ipsum dolor sit amet, consectetur adipiscing elit. Ut nibh leo, cursus et laoreet ac, lobortis vulputate orci. Nunc ultricies massa egestas malesuada pretium. Morbi congue sem ultricies dui lobortis dictum. Ut convallis quam diam, vel interdum dolor semper et. Morbi tincidunt fermentum sem sit amet iaculis. Sed ullamcorper egestas metus, quis luctus magna venenatis id. Aenean ultricies enim eget magna convallis, aliquet venenatis nisi varius. Sed varius eu lectus nec ullamcorper. Praesent ullamcorper, nulla sed lobortis ultrices, urna mi tincidunt turpis, non maximus eros ex ut eros. Aliquam tincidunt ut odio sed mollis. In et ante in nibh iaculis gravida. In arcu</p>
    </div>
  </div>

  <div class="abs color-strip"></div>
</section>

</body>
</html>
```